Harrow's Electrical & Solar - Business Cards

I want my business card to stand out from the rest. I will provide my business name logo and my icon logo to be implemented onto the card.

On the front of the card, can i have the following. Just make it neat & professional please.

Liam Corbett
harrowselectrical@quillmail.test
0438 917 605
ABN: 41 602 719 384
License No. 582164K
FREE QUOTES
24/7 Emergency

On the back of the card, can I have "Our Services" and maybe add the S logo on the back in the background or something. Under "Our Services" I want the following:

LED Lighting Upgrades
Switches & Outlets
Smoke Alarms
Switchboard Upgrades
Fault Finding
Rewiring
New Builds
Test & Tagging
All Electrical Maintenance & Repairs

Can you guys add the instagram logo and next to it, put harrows_electrical

Can you guys also add the facebook logo and next to it put Harrow's Electrical & Solar. Make sure the instagram & facebook icon is in either white, green or black.

Also I have put down double sided, not sure why when i save it, it keeps going to single sided. I need my business card double sided.

Target Market(s)

New Customers

Contact Information for Business Card

Liam Corbett harrowselectrical@quillmail.test 0438 917 605 ABN: 41 602 719 384 License No. 582164K FREE QUOTES 24/7 Emergency

Requirements
Must have
• must be tidy, professional and appealing

```html
<!DOCTYPE html>
<html lang="en">
<head>
<meta charset="utf-8">
<title>Harrow's Electrical &amp; Solar – Business Cards</title>
<link rel="stylesheet" href="https://fonts.googleapis.com/css2?family=Montserrat:wght@400;500;600;700&family=Russo+One&display=swap">
<style>
  :root {
    --stage: #d6d6d6;
    --card: #050505;
    --green: #2fcf3c;
    --green-deep: #1f8f2a;
    --green-faint: rgba(47, 207, 60, 0.10);
    --white: #f2f2f2;
    --grey: #bfc3c7;
  }
  * { box-sizing: border-box; margin: 0; padding: 0; }
  html, body { width: 1200px; height: 913px; overflow: hidden; }
  body {
    background: var(--stage);
    font-family: "Montserrat", sans-serif;
    color: var(--white);
    position: relative;
  }
  .card {
    position: absolute;
    left: 250px;
    width: 700px;
    height: 400px;
    background: var(--card);
    border: 2px solid var(--green);
    overflow: hidden;
    box-shadow: 0 14px 30px rgba(0, 0, 0, 0.35);
  }
  .card--front { top: 40px; }
  .card--back { top: 473px; }

  /* Front */
  .front__ring {
    position: absolute;
    left: 330px; top: 30px;
    width: 340px; height: 340px;
    border-radius: 50%;
    border: 14px solid var(--green-faint);
  }
  .brand {
    position: absolute;
    left: 40px; top: 44px;
    display: flex; align-items: center; gap: 12px;
  }
  .brand__dot {
    width: 30px; height: 30px; border-radius: 50%;
    background: var(--green);
  }
  .brand__name {
    font-weight: 700; font-size: 22px; color: var(--white);
    letter-spacing: 0.5px;
  }
  .person {
    position: absolute; left: 110px; top: 120px;
  }
  .person__name {
    font-family: "Russo One", sans-serif;
    color: var(--green); font-size: 34px; letter-spacing: 0.5px;
  }
  .person__title { font-size: 17px; font-weight: 500; margin-top: 2px; }
  .front__divider {
    position: absolute; left: 110px; right: 40px; top: 206px;
    height: 1.5px; background: var(--green);
  }
  .contacts {
    position: absolute; left: 110px; top: 224px;
    list-style: none; font-size: 17px; font-weight: 500;
  }
  .contacts li {
    display: flex; align-items: center; gap: 12px; height: 34px;
  }
  .contacts svg { width: 18px; height: 18px; flex: none; }
  .contacts .social-mark {
    width: 16px; height: 16px; border-radius: 50%;
    border: 2.5px solid var(--green); flex: none; margin: 0 1px;
  }
  .credentials {
    position: absolute; right: 40px; top: 224px;
    text-align: right; font-size: 16px; font-weight: 500; line-height: 30px;
  }
  .credentials .highlight { color: var(--green); }

  /* Back */
  .back__emblem {
    position: absolute; left: 0; right: 0; top: 40px;
    display: flex; flex-direction: column; align-items: center; gap: 12px;
  }
  .back__circle {
    width: 110px; height: 110px; border-radius: 50%;
    border: 8px solid var(--green);
  }
  .back__name { font-weight: 700; font-size: 20px; color: var(--white); }
  .services {
    position: absolute; left: 40px; right: 40px; top: 218px;
    text-align: center;
  }
  .services__heading {
    display: flex; align-items: center; gap: 16px;
  }
  .services__heading::before,
  .services__heading::after {
    content: ""; flex: 1; height: 1.5px; background: var(--green);
  }
  .services__title {
    font-family: "Russo One", sans-serif; color: var(--green);
    font-size: 30px; font-weight: 400;
  }
  .services__list {
    margin-top: 12px; font-size: 17px; font-weight: 500; line-height: 30px;
  }
  .bullet { color: var(--green); margin: 0 6px; font-size: 14px; }
</style>
</head>
<body>

<section class="card card--front" aria-label="Business card front">
  <div class="front__ring"></div>

  <div class="brand">
    <span class="brand__dot"></span>
    <span class="brand__name">Harrow's Electrical &amp; Solar</span>
  </div>

  <div class="person">
    <h1 class="person__name">Liam Corbett</h1>
    <p class="person__title">Managing Director</p>
  </div>

  <div class="front__divider"></div>

  <ul class="contacts">
    <li>
      <svg viewBox="0 0 24 24" aria-hidden="true"><path fill="#2fcf3c" d="M6.6 10.8a15.1 15.1 0 0 0 6.6 6.6l2.2-2.2a1 1 0 0 1 1-.25 11.4 11.4 0 0 0 3.6.57 1 1 0 0 1 1 1V20a1 1 0 0 1-1 1A17 17 0 0 1 3 4a1 1 0 0 1 1-1h3.5a1 1 0 0 1 1 1c0 1.25.2 2.45.57 3.57a1 1 0 0 1-.25 1z"/></svg>
      0438 917 605
    </li>
    <li>
      <svg viewBox="0 0 24 24" aria-hidden="true"><rect x="2" y="5" width="20" height="14" rx="1.5" fill="#2fcf3c"/><path d="M3 6l9 7 9-7" fill="none" stroke="#050505" stroke-width="1.8"/></svg>
      harrowselectrical@quillmail.test
    </li>
    <li><span class="social-mark"></span>Harrow's Electrical &amp; Solar</li>
    <li><span class="social-mark"></span>harrows_electrical</li>
  </ul>

  <div class="credentials">
    <p>ABN: 41 602 719 384</p>
    <p>License No. 582164K</p>
    <p class="highlight">FREE QUOTES</p>
    <p class="highlight">24/7 Emergency</p>
  </div>
</section>

<section class="card card--back" aria-label="Business card back">
  <div class="back__emblem">
    <span class="back__circle"></span>
    <span class="back__name">Harrow's Electrical &amp; Solar</span>
  </div>

  <div class="services">
    <div class="services__heading"><h2 class="services__title">Our Services</h2></div>
    <p class="services__list">
      <span class="bullet">●</span>LED Lighting Upgrades <span class="bullet">●</span>Switches &amp; Outlets<br>
      <span class="bullet">●</span>Smoke Alarms <span class="bullet">●</span>Switchboard Upgrades <span class="bullet">●</span>Fault Finding<br>
      <span class="bullet">●</span>Rewiring <span class="bullet">●</span>New Builds <span class="bullet">●</span>Test &amp; Tagging<br>
      <span class="bullet">●</span>All Electrical Maintenance &amp; Repairs
    </p>
  </div>
</section>

</body>
</html>
```